Animal Facility Brochure for Pet Boarding, Boutique, Doggie Daycare, Grooming

This brochure is for a Doggie Daycare, Pet Grooming, Dog Boarding & Pet Boutique for the Hollowmere Pet Lodge & Spa.

Hi there! I am in need of a brochure done for my new up and coming business.
The business will involve Dog/Cat Grooming, Dog Boarding, Doggie Daycare, & a small pet boutique. I am looking for something that stands out and is modern and chic and follows the look of the pictures i have posted (Pim and Tessel) . My color scheme of my business is gray & white. Also i need the brochure to be easily able to understand what we are trying to get across and is easy to read. I am very proud of my logo that was created using craft hive and would love that incorporated. also i have attached the information that will need to be in the brochure for the client. I am looking for someone who can devote some time working with me on this because this is my first time. I am sure there will need to be some changes so i need someone who is patient. The picture of the projected look of my sign is gearing more towards something clean and modern.

Industry/Entity Type

Pet Care

Colors
f5f5f5
f8f8f8
dbdbdb
959595
aaaaaa
85abd2
cedeed
eaf1f7

Requirements
Nice to have
• File nine for Grooming, Boarding, Daycare, Pet Boutique

```html
<!DOCTYPE html>
<html lang="en">
<head>
<meta charset="utf-8">
<title>Hollowmere Pet Lodge &amp; Spa – Trifold Brochure</title>
<link href="https://fonts.googleapis.com/css2?family=Archivo+Narrow:wght@400;500&family=Italianno&display=swap" rel="stylesheet">
<style>
  :root {
    --page: #eeeeee;
    --paper: #f8f8f8;
    --paper-shade: #dbdbdb;
    --charcoal: #5a5a5a;
    --charcoal-dark: #3f3f3f;
    --sky: #85abd2;
    --sky-deep: #5f86b4;
    --sky-pale: #cedeed;
    --sky-mist: #eaf1f7;
    --ink: #2b2b2b;
    --brown: #4a3426;
    --white: #ffffff;
  }
  * { box-sizing: border-box; margin: 0; padding: 0; }
  html, body { width: 821px; height: 1200px; overflow: hidden; }
  body {
    background: var(--page);
    font-family: "Archivo Narrow", Arial, sans-serif;
    color: var(--ink);
    position: relative;
  }
  .brochure {
    position: absolute;
    left: 20px; top: 322px;
    width: 780px; height: 556px;
    display: flex;
    box-shadow: 0 6px 20px rgba(0,0,0,.18);
  }
  .panel {
    position: relative;
    width: 260px; height: 556px;
    overflow: hidden;
  }
  .panel-art { position: absolute; inset: 0; width: 260px; height: 556px; }

  /* mission panel */
  .mission-tab {
    position: absolute; left: 0; top: 18px;
    width: 122px; height: 26px;
    background: var(--charcoal);
    border-radius: 0 13px 13px 0;
    color: var(--white);
    font-family: "Italianno", cursive;
    font-weight: 400;
    font-size: 24px; line-height: 26px;
    padding-left: 24px;
  }
  .mission-text {
    position: absolute; left: 22px; top: 56px; width: 226px;
    font-size: 12px; line-height: 16.4px;
    text-align: justify;
  }
  .call-us {
    position: absolute; left: 20px; top: 340px;
    color: var(--ink);
  }
  .call-us .label {
    display: block;
    font-family: "Italianno", cursive; font-weight: 400;
    font-size: 24px; line-height: 22px;
  }
  .call-us .number {
    display: block;
    font-family: "Archivo Narrow", sans-serif; font-weight: 400;
    font-size: 18px; line-height: 22px; letter-spacing: .5px;
  }

  .photo {
    position: absolute;
    border-radius: 4px;
  }
  .photo-dog-cat {
    left: 8px; top: 386px; width: 246px; height: 164px;
    background: radial-gradient(ellipse at 60% 55%, #d9cbb8 0%, #b7a48f 45%, rgba(183,164,143,0) 72%);
  }

  /* brand mark */
  .brand {
    position: absolute; left: 0; right: 0;
    display: flex; flex-direction: column; align-items: center;
    color: var(--brown);
    font-family: "Archivo Narrow", sans-serif; font-weight: 500;
    text-transform: uppercase; text-align: center;
  }
  .brand .dot { border-radius: 50%; background: var(--brown); }
  .brand-small { top: 22px; font-size: 9px; line-height: 11px; }
  .brand-small .dot { width: 22px; height: 22px; margin-bottom: 5px; }
  .brand-large { top: 34px; font-size: 15px; line-height: 18px; letter-spacing: .5px; }
  .brand-large .dot { width: 40px; height: 40px; margin-bottom: 10px; }

  /* info panel */
  .section-title {
    position: absolute; left: 0; right: 0; text-align: center;
    font-family: "Italianno", cursive; font-weight: 400;
    color: var(--sky);
    font-size: 22px; line-height: 22px;
  }
  .title-contact { top: 146px; }
  .title-hours { top: 252px; }
  .contact-list { position: absolute; left: 20px; top: 170px; width: 230px; list-style: none; color: var(--white); font-size: 10px; }
  .contact-list li { display: flex; align-items: flex-start; gap: 10px; margin-bottom: 6px; line-height: 12.5px; }
  .contact-list svg { flex: none; margin-top: 1px; }
  .contact-list .indent { padding-left: 52px; }
  .hours {
    position: absolute; left: 46px; top: 276px; width: 190px;
    table-layout: fixed;
    color: var(--white); font-size: 10px; border-collapse: collapse;
  }
  .hours td { height: 17.3px; padding: 0; white-space: nowrap; overflow: hidden; }
  .hours .day { width: 92px; padding-right: 4px; }
  .hours .day span::after { content: " ................................"; }
  .photo-treat-bag {
    left: 92px; top: 404px; width: 76px; height: 108px;
    background: linear-gradient(180deg, #b8a07f, #9e8462);
    border-radius: 18px 18px 6px 6px;
  }

  .web-pill {
    position: absolute; left: 20px; width: 220px; top: 520px; height: 22px;
    border-radius: 11px; border: 1px solid #9a9a9a;
    background: var(--charcoal-dark);
    color: var(--white); font-size: 10.5px; letter-spacing: .6px;
    text-align: center; line-height: 20px;
  }

  /* cover panel */
  .photo-puppy-kitten {
    left: 0; top: 162px; width: 260px; height: 220px; border-radius: 0;
    background: linear-gradient(180deg, #4f6a34 0%, #6f8b3f 45%, #8fa651 70%, #e4d9c0 100%);
  }
  .tagline {
    position: absolute; left: 14px; right: 14px; top: 420px;
    text-align: center; color: var(--white);
    font-family: "Italianno", cursive; font-weight: 400;
    font-size: 20px; line-height: 20px;
  }
  .tagline-accent {
    position: absolute; left: 0; right: 0; top: 460px;
    text-align: center; color: var(--white);
    font-family: "Italianno", cursive; font-weight: 400;
    font-size: 44px; line-height: 44px;
  }
</style>
</head>
<body>
<main class="brochure">

  <!-- Mission panel -->
  <section class="panel panel-mission">
    <svg class="panel-art" viewBox="0 0 260 556" aria-hidden="true">
      <defs>
        <linearGradient id="paperFade" x1="0" y1="0" x2="1" y2="0">
          <stop offset="0" stop-color="#dcdcdc"/>
          <stop offset=".25" stop-color="#f8f8f8"/>
          <stop offset="1" stop-color="#ffffff"/>
        </linearGradient>
        <linearGradient id="blueBand1" x1="0" y1="0" x2="0" y2="1">
          <stop offset="0" stop-color="#85abd2"/>
          <stop offset="1" stop-color="#5f86b4"/>
        </linearGradient>
      </defs>
      <rect width="260" height="556" fill="url(#paperFade)"/>
      <path d="M0 405 C70 430 140 470 260 470 L260 556 L0 556 Z" fill="#3f3f3f"/>
      <path d="M0 418 C70 445 140 480 260 478 L260 556 L0 556 Z" fill="#ffffff"/>
      <path d="M0 428 C80 458 150 490 260 488 L260 556 L0 556 Z" fill="url(#blueBand1)"/>
    </svg>
    <h2 class="mission-tab">Our Mission:</h2>
    <p class="mission-text">Our mission is to care for your pet in the best way possible when you are away. We provide a unique social experience for dogs and create a new standard for dog care. Our Kitty condo provides a safe and quiet atmosphere for your kitty. We have set out to create a facility that exemplifies what we ourselves would want for our own best friends. Your pet will have a fun, safe place to play during the day and a secure night time environment when lodging with us. Our staff will go to any lengths to make our guest's stay a true delight. Our professional spa and grooming salon offers a wide range of services for your dog and cat. Our experienced groomers are friendly and knowledgeable and have the expertise to help your pet look and feel its best while exceeding your expectations.</p>
    <p class="call-us"><span class="label">Call Us:</span><span class="number">555-218-4407</span></p>
    <div class="photo photo-dog-cat" role="img" aria-label="Photo of a terrier puppy sitting beside a lounging tabby cat"></div>
  </section>

  <!-- Info panel -->
  <section class="panel panel-info">
    <svg class="panel-art" viewBox="0 0 260 556" aria-hidden="true">
      <defs>
        <linearGradient id="skyTop" x1="0" y1="0" x2="0" y2="1">
          <stop offset="0" stop-color="#cedeed"/>
          <stop offset="1" stop-color="#ffffff"/>
        </linearGradient>
        <linearGradient id="charcoalFill" x1="0" y1="0" x2="0" y2="1">
          <stop offset="0" stop-color="#4a4a4a"/>
          <stop offset="1" stop-color="#6a6a6a"/>
        </linearGradient>
        <linearGradient id="blueBand2" x1="0" y1="0" x2="1" y2="0">
          <stop offset="0" stop-color="#5f86b4"/>
          <stop offset="1" stop-color="#85abd2"/>
        </linearGradient>
      </defs>
      <rect width="260" height="556" fill="url(#skyTop)"/>
      <path d="M0 112 C90 100 170 100 260 125 L260 556 L0 556 Z" fill="#5f86b4"/>
      <path d="M0 118 C90 108 170 110 260 132 L260 556 L0 556 Z" fill="#ffffff"/>
      <path d="M0 124 C90 116 170 120 260 140 L260 556 L0 556 Z" fill="url(#charcoalFill)"/>
      <path d="M0 500 C80 470 170 450 260 440 L260 556 L0 556 Z" fill="#ffffff"/>
      <path d="M0 508 C80 480 170 458 260 448 L260 556 L0 556 Z" fill="url(#blueBand2)"/>
    </svg>
    <div class="brand brand-small"><span class="dot"></span>Hollowmere Pet<br>Lodge &amp; Spa</div>

    <h3 class="section-title title-contact">Contact Details</h3>
    <ul class="contact-list">
      <li><svg width="10" height="10" viewBox="0 0 10 10"><circle cx="5" cy="5" r="5" fill="#fff"/><path d="M2.5 5.2 L5 3 L7.5 5.2 V7.3 H2.5 Z" fill="#5a5a5a"/></svg><span>48 Alder Mill Road<br>Hollowmere, OH 43990</span></li>
      <li class="indent"><svg width="10" height="10" viewBox="0 0 10 10"><rect width="10" height="10" rx="2" fill="#fff"/><rect x="3" y="1.8" width="4" height="6.4" rx=".8" fill="#5a5a5a"/></svg><span>555-218-4407</span></li>
      <li><svg width="10" height="10" viewBox="0 0 10 10"><circle cx="5" cy="5" r="5" fill="#fff"/><rect x="2.3" y="3.2" width="5.4" height="3.6" fill="#5a5a5a"/></svg><span>info@hollowmerepetlodgeandspa.com</span></li>
    </ul>

    <h3 class="section-title title-hours">Hours of Operation</h3>
    <table class="hours">
      <tr><td class="day"><span>Monday</span></td><td>7:00am- 7:00pm</td></tr>
      <tr><td class="day"><span>Tuesday</span></td><td>7:00am- 7:00pm</td></tr>
      <tr><td class="day"><span>Wednesday</span></td><td>7:00am- 7:00pm</td></tr>
      <tr><td class="day"><span>Thursday</span></td><td>7:00am- 7:00pm</td></tr>
      <tr><td class="day"><span>Friday</span></td><td>7:00am- 7:00pm</td></tr>
      <tr><td class="day"><span>Saturday</span></td><td>9:00am- 5:00pm</td></tr>
      <tr><td class="day"><span>Sunday</span></td><td>11:00am- 4:00pm</td></tr>
    </table>

    <div class="photo photo-treat-bag" role="img" aria-label="Photo of a burlap drawstring bag of dog treats"></div>
    <p class="web-pill">www.hollowmerepetlodgeandspa.com</p>
  </section>

  <!-- Cover panel -->
  <section class="panel panel-cover">
    <svg class="panel-art" viewBox="0 0 260 556" aria-hidden="true">
      <defs>
        <linearGradient id="skyTop2" x1="0" y1="0" x2="0" y2="1">
          <stop offset="0" stop-color="#cedeed"/>
          <stop offset=".6" stop-color="#eaf1f7"/>
          <stop offset="1" stop-color="#ffffff"/>
        </linearGradient>
        <linearGradient id="blueBand3" x1="0" y1="0" x2="0" y2="1">
          <stop offset="0" stop-color="#6f95c1"/>
          <stop offset="1" stop-color="#4f76a5"/>
        </linearGradient>
      </defs>
      <rect width="260" height="556" fill="url(#skyTop2)"/>
      <rect y="160" width="260" height="396" fill="#6f8b3f"/>
    </svg>
    <div class="photo photo-puppy-kitten" role="img" aria-label="Photo of a golden retriever puppy lying on the grass beside a small tabby kitten"></div>
    <svg class="panel-art" viewBox="0 0 260 556" aria-hidden="true">
      <path d="M0 150 C80 130 170 140 260 120 L260 0 L0 0 Z" fill="url(#skyTop2)"/>
      <path d="M0 150 C80 130 170 140 260 120 L260 130 C170 152 80 142 0 164 Z" fill="#5f86b4"/>
      <path d="M0 164 C80 142 170 152 260 130 L260 138 C170 160 80 152 0 172 Z" fill="#3f3f3f"/>
      <path d="M0 375 C80 365 170 360 260 330 L260 556 L0 556 Z" fill="#3f3f3f"/>
      <path d="M0 383 C80 374 170 370 260 342 L260 556 L0 556 Z" fill="#ffffff"/>
      <path d="M0 392 C80 384 170 382 260 354 L260 556 L0 556 Z" fill="url(#blueBand3)"/>
    </svg>
    <div class="brand brand-large"><span class="dot"></span>Hollowmere Pet<br>Lodge &amp; Spa</div>
    <p class="tagline">When it comes to your pet, we will stop at nothing to keep them healthy, happy and</p>
    <p class="tagline-accent">Well-Loved</p>
    <p class="web-pill">www.hollowmerepetlodgeandspa.com</p>
  </section>

</main>
</body>
</html>
```